Website Design for Chef Wirra Chinese Restaurant

Chef Wirra is a new Chinese Restaurant. It offers exceptional dining experience with authentic and dynamic dishes created with quality ingredients.

A vivid website theme is required to promote this new restaurant online. Logo, menu, wine list and a few other files are attached for help with designing.

A very rough demo website has been setup and can be accessed via http://www.chefwirra.com.au. It is for telling designers what content is shown up on each page (except for homepage). By reading the about us page, designers can get some more info of Chef Wirra. However, the layout, theme color, font, etc are not set in stone. Visitors should be able to feel Chef Wirra restaurant's authentic Chinese cuisine and high hygiene standard. Home page of the website could be The "Our website is coming soon" description is shown on demo site but do not required to be presented on new design.

Some main pages design should be included: Home (landing page), About us, Menu (Dishes), Winelist, Gallery, Contact us. No HTML and coding required. The output should be well layered psd or png files with acceptable resolution for web use.

A few other website can be referred to are:

http://kelpmerachinese.com.au/
http://www.stone-lamp.com/
http://brimvale.com.au/
http://harvelrestaurant.com.au/
http://www.tilmorerestaurant.com.au/
http://www.thequill.com.au/

Industry/Entity Type

Restaurant

Requirements
Nice to have
• I expect designs of at least these webpages: homepage, menu page and contact us page. If you can provide "about us" page as well, it will probably help you win the competition. well layered psd or png file is my preference.
Should not have
• You don't have to make html/cs/js or any coding. All I need is just art design

```html
<!DOCTYPE html>
<html lang="en">
<head>
<meta charset="utf-8">
<title>Chef Wirra Chinese Restaurant</title>
<link href="https://fonts.googleapis.com/css2?family=Arimo:wght@400;700&family=Noto+Sans+SC:wght@400&display=swap" rel="stylesheet">
<style>
:root{
  --crimson:#8e1420;
  --crimson-dark:#5a0a10;
  --gold:#f0c75a;
  --paper:#f3f2f2;
  --ink:#3b0c0c;
  --white:#ffffff;
  --pink:#e79ab0;
}
*{box-sizing:border-box;margin:0;padding:0}
html,body{width:1200px;height:1152px;overflow:hidden;background:var(--white);font-family:"Arimo",Arial,sans-serif}
.page{position:relative;width:1200px;height:1152px}
.header{position:absolute;left:6px;top:4px;width:1188px;height:60px;background:linear-gradient(#a31d2a,#7b1019)}
.brand{position:absolute;left:76px;top:10px;display:flex;align-items:center;gap:10px;color:var(--white);font-size:23px}
.brand-mark{width:22px;height:22px;background:var(--white)}
.phone{position:absolute;left:705px;top:8px;display:flex;align-items:center;gap:6px;color:var(--white);font-size:23px}
.search{position:absolute;left:900px;top:12px;display:flex}
.search-field{width:184px;height:20px;border-radius:10px 0 0 10px;background:linear-gradient(#fff,#d8d8d8);font-size:10px;color:#555;padding:5px 14px}
.search-go{width:40px;height:20px;border-radius:0 10px 10px 0;background:var(--crimson-dark);color:var(--white);font-size:11px;font-weight:700;text-align:center;line-height:20px}
.nav{position:absolute;left:6px;top:64px;width:1188px;height:42px;background:linear-gradient(#6b0a12,#4a060b);display:flex;padding-left:90px}
.nav a{color:var(--white);text-decoration:none;font-size:14px;font-weight:700;padding:13px 18px;border-right:1px solid #7a1a20}
.nav a.active{border-bottom:3px solid var(--pink)}
.hero-band{position:absolute;left:6px;top:106px;width:1188px;height:252px;background:var(--crimson)}
.hero{position:absolute;left:69px;top:106px;width:1062px;height:252px;background:radial-gradient(ellipse at 50% 55%,#d27a2c,#8a3c14 55%,#d7c8b4)}
.dots{position:absolute;left:1025px;top:339px;display:flex;gap:8px}
.dots span{width:11px;height:11px;border-radius:50%;background:var(--white)}
.dots span.on{background:#f2a51c}
.content{position:absolute;left:26px;top:358px;width:1124px;height:634px;background:var(--paper)}
.sidebar{position:absolute;left:35px;top:358px;width:245px}
.sidebar h2{font-size:22px;font-weight:400;color:var(--ink);padding:9px 0 6px 35px;background:var(--white)}
.cat{height:33px;margin-bottom:3px;background:linear-gradient(#f6eeee,#b4404f 45%,#7c0f1e);font-size:16px;font-weight:700;color:#2a0606;padding:7px 35px}
.main-title{position:absolute;left:326px;top:362px;font-size:28px;font-weight:400;color:var(--ink);letter-spacing:.2px}
.photo{position:absolute;left:320px;width:270px}
.photo-hall{top:410px;height:197px;background:linear-gradient(170deg,#e8b45a 0%,#c8702a 30%,#8e1b14 60%,#b04a2a 80%,#f1e6da 100%)}
.photo-table{top:618px;height:191px;background:linear-gradient(#2e2a2a 0%,#c8302a 30%,#d8a27a 55%,#7a1a16 75%,#c9c2b0 100%)}
.photo-map{top:820px;height:155px;background:linear-gradient(135deg,#e9e5d6,#dcd8c6 50%,#ece8da);border:1px solid #e11}
.copy{position:absolute;left:600px;top:406px;width:536px;font-size:16px;line-height:20.5px;color:var(--ink);word-break:break-all}
.copy p+p{margin-top:20px}
.bar{position:absolute;left:600px;width:529px;height:27px;background:var(--gold);color:var(--ink);font-size:16px;padding:4px 24px}
.bar-hours{top:620px}.bar-location{top:832px}
.hours{position:absolute;left:625px;top:654px;font-size:16px;line-height:20.5px;color:var(--ink)}
.location{position:absolute;left:623px;top:868px;font-size:16px;line-height:20.5px;color:var(--ink)}
.social-handle{position:absolute;left:798px;top:922px;font-family:"Noto Sans SC",sans-serif;font-size:20px;color:#222}
.social-url{position:absolute;left:624px;top:950px;font-size:22px;letter-spacing:1px;color:#222}
.footer{position:absolute;left:6px;top:992px;width:1188px;height:160px;background:var(--crimson)}
.footer h3{position:absolute;font-size:27px;font-weight:400;color:var(--white);top:24px}
.footer ul{position:absolute;list-style:none;font-size:16px;line-height:20px;color:var(--white)}
.col-company h3,.col-company ul{left:65px}
.col-company ul{top:74px}
.col-links h3{left:314px}.col-links ul{left:316px;top:84px}
.news h3{left:594px}
.news-field{position:absolute;left:594px;top:67px;width:207px;height:28px;border-radius:14px;background:var(--white)}
.subscribe{position:absolute;left:687px;top:106px;width:110px;height:22px;border-radius:11px;background:var(--pink);font-size:13px;text-align:center;line-height:22px;color:#222}
.icons{position:absolute;left:852px;top:22px;display:flex;gap:20px}
.icons span{width:38px;height:38px;border-radius:6px;background:#b81a22;box-shadow:0 2px 3px rgba(0,0,0,.4)}
</style>
</head>
<body>
<div class="page">
  <header class="header">
    <div class="brand"><span class="brand-mark"></span><span>Chef Wirra Chinese Restaurant</span></div>
    <div class="phone">
      <svg width="20" height="26" viewBox="0 0 20 26"><path d="M5 2h5l1 6-3 2c1 4 3 7 6 8l2-3 4 3-2 6c-9-1-15-10-14-20z" fill="#222"/></svg>
      <span>(08) 8555 0142</span>
    </div>
    <div class="search"><div class="search-field">Search</div><div class="search-go">GO</div></div>
  </header>
  <nav class="nav">
    <a class="active">Home</a><a>Menu</a><a>About us</a><a>Wine List</a><a>Gallery</a><a>Contact us</a>
  </nav>
  <div class="hero-band"></div>
  <div class="hero" role="img" aria-label="Glazed chicken wings garnished with coriander"></div>
  <div class="dots"><span></span><span></span><span></span><span class="on"></span></div>

  <div class="content"></div>
  <aside class="sidebar">
    <h2>Menu Category</h2>
    <div class="cat">Beer &amp; Cider</div>
    <div class="cat">Cocktail</div>
    <div class="cat">Spirits</div>
    <div class="cat">Non Alcoholic</div>
    <div class="cat">Traditonal Tea</div>
    <div class="cat">Coffee &amp; Chocolate</div>
    <div class="cat">Wine By the Glass</div>
    <div class="cat">Wines</div>
    <div class="cat">Dessert Wines</div>
    <div class="cat">Fortifieds &amp; Cognac</div>
  </aside>

  <h1 class="main-title">Welcome to Chef Wirra Chinese Restaurant</h1>
  <div class="photo photo-hall" role="img" aria-label="Restaurant dining hall with round tables and chandeliers"></div>
  <div class="photo photo-table" role="img" aria-label="Guests sharing a banquet at a round table"></div>
  <div class="photo photo-map" role="img" aria-label="Street map showing the restaurant location"></div>

  <div class="copy">
    <p>Welcome to our new website! Chef Wirra Restaurant is renowned for hosting the best Yum Cha in town.Being in the industry for over 10 years, Chef Wirra Restaurant has gained its reputation through friendly hospitality, combined with a modern and elegant Chinese ambience.</p>
    <p>You will always be pampered with Chef Wirra's vast variety of Yum Cha a showcasing more than 90 items to order. Either for casual dining, quick take away, or holding an event, our extensive and always fresh menu selections are designed to impress.</p>
  </div>

  <div class="bar bar-hours">Trading Hours</div>
  <div class="hours">
    We are open 7 days<br><br>
    Lunch:<br>Monday to Friday 11:30am – 2:30pm<br>Saturday to Sunday 11:00am – 3:00pm<br><br>
    Dinner:<br>Monday to Sunday 6:00pm Until Late
  </div>
  <div class="bar bar-location">Location</div>
  <div class="location">Add:30/10s Marlowe Road<br>St. Aldens SA 5069<br>Fully Licensed</div>
  <div class="social-handle">@金灯笼</div>
  <div class="social-url">lanternpost.com/u/4702196358</div>

  <footer class="footer">
    <div class="col-company"><h3>Company</h3><ul><li>About Us</li><li>Contact Us</li><li>Customer Servic</li><li>Privacy Policy</li></ul></div>
    <div class="col-links"><h3>Quicks Links</h3><ul><li>Site Map</li><li>Search Terms</li><li>Advanced Search</li></ul></div>
    <div class="news"><h3>News Letter</h3><div class="news-field"></div><div class="subscribe">Subscribe</div></div>
    <div class="icons"><span></span><span></span><span></span></div>
  </footer>
</div>
</body>
</html>
```